Business card design for Allied Healthcare provider

We would like a design for front and back of business cards. The design must resonate with all levels of customers from patients, to other health providers and medical. Must also resonate with corporate customers

Target Market(s)

patients, medical practitioners, other health providers and corporate.

Industry/Entity Type

healthcare

Contact Information for Business Card

name, logo, phone and fax numbers, email, website

Requirements
Must have
• not allowing me to change this, but the card must be double sided!! Please take note
Nice to have
• a fresh yet bold design to catch attention.

```html
<!DOCTYPE html>
<html lang="en">
<head>
<meta charset="utf-8">
<title>Vitalane — Business Card, Front and Back</title>
<link href="https://fonts.googleapis.com/css2?family=Poppins:wght@400;500;600;700&display=swap" rel="stylesheet">
<style>
  :root {
    --stage: #2e2f31;
    --navy: #1a2c5b;
    --navy-deep: #14234b;
    --navy-light: #24408a;
    --gold: #f5ad1b;
    --ink: #1a2c5b;
    --paper: #ffffff;
  }
  * { box-sizing: border-box; margin: 0; padding: 0; }
  html, body { width: 1200px; height: 1015px; overflow: hidden; }
  body {
    background: var(--stage);
    font-family: "Poppins", sans-serif;
    display: flex;
    flex-direction: column;
    align-items: center;
    justify-content: center;
    gap: 47px;
  }
  .card {
    position: relative;
    width: 760px;
    height: 434px;
    overflow: hidden;
    box-shadow: 0 14px 30px rgba(0,0,0,.45);
  }

  /* Back side */
  .card--back { background: var(--navy); }
  .card__pattern {
    position: absolute; inset: 0;
    background: radial-gradient(ellipse at 70% 20%, var(--navy-light) 0%, var(--navy) 45%, var(--navy-deep) 100%);
  }
  .card--back .wordmark {
    position: absolute; left: 50%; top: 50%;
    transform: translate(-50%, -50%);
    color: var(--paper);
    font-size: 46px;
  }

  /* Shared wordmark */
  .wordmark {
    display: flex; align-items: center; gap: 14px;
    font-weight: 600; letter-spacing: 0.5px; line-height: 1;
  }
  .wordmark__dot {
    width: 22px; height: 22px; border-radius: 50%;
    background: var(--gold); flex: none;
  }

  /* Front side */
  .card--front { background: var(--paper); }
  .card--front .wordmark {
    position: absolute; left: 58px; top: 196px;
    color: var(--ink);
    font-size: 44px;
  }
  .contact {
    position: absolute; left: 448px; top: 96px;
    color: var(--ink);
  }
  .contact__identity {
    position: relative; padding-left: 16px; margin-bottom: 26px;
  }
  .contact__identity::before {
    content: ""; position: absolute; left: 0; top: 4px; bottom: 4px;
    width: 3px; background: var(--gold);
  }
  .contact__name {
    color: var(--gold); font-weight: 700; font-size: 30px; line-height: 1.1;
  }
  .contact__role { font-size: 15px; font-weight: 400; margin-top: 4px; }
  .contact__list {
    list-style: none; position: relative; padding-left: 16px;
  }
  .contact__list::before {
    content: ""; position: absolute; left: 0; top: 2px; bottom: 2px;
    width: 3px; background: var(--navy);
  }
  .contact__item {
    display: flex; align-items: center; gap: 10px;
    font-size: 16px; line-height: 1; margin-bottom: 12px;
  }
  .contact__item:last-child { margin-bottom: 0; }
  .contact__icon { width: 18px; height: 18px; flex: none; }
  .contact__accent { color: var(--gold); }
</style>
</head>
<body>

  <section class="card card--back" aria-label="Card back">
    <div class="card__pattern" role="img" aria-label="Embossed repeating monogram pattern in tonal navy blue"></div>
    <div class="wordmark">
      <span class="wordmark__dot"></span>
      <span class="wordmark__name">Vitalane</span>
    </div>
  </section>

  <section class="card card--front" aria-label="Card front">
    <div class="wordmark">
      <span class="wordmark__dot"></span>
      <span class="wordmark__name">Vitalane</span>
    </div>

    <div class="contact">
      <div class="contact__identity">
        <p class="contact__name">Daniel Reyes</p>
        <p class="contact__role">Managing Director</p>
      </div>
      <ul class="contact__list">
        <li class="contact__item">
          <svg class="contact__icon" viewBox="0 0 24 24" aria-hidden="true"><path fill="#f5ad1b" d="M6.6 10.8a15.1 15.1 0 0 0 6.6 6.6l2.2-2.2c.3-.3.7-.4 1-.2 1.1.4 2.3.6 3.6.6.6 0 1 .4 1 1V20c0 .6-.4 1-1 1A17 17 0 0 1 3 4c0-.6.4-1 1-1h3.5c.6 0 1 .4 1 1 0 1.3.2 2.5.6 3.6.1.3 0 .7-.2 1z"/></svg>
          <span>021-555 0148</span>
        </li>
        <li class="contact__item">
          <svg class="contact__icon" viewBox="0 0 24 24" aria-hidden="true"><path fill="#f5ad1b" d="M6 2h12v6H6zM3 9h18a1 1 0 0 1 1 1v7h-4v5H6v-5H2v-7a1 1 0 0 1 1-1zm5 7v4h8v-4z"/></svg>
          <span>021-555 0149</span>
        </li>
        <li class="contact__item">
          <svg class="contact__icon" viewBox="0 0 24 24" aria-hidden="true"><path fill="#f5ad1b" d="M2 5h20v14H2zm2 2v.5l8 5 8-5V7z"/></svg>
          <span>hello@vitalane.com</span>
        </li>
        <li class="contact__item">
          <svg class="contact__icon" viewBox="0 0 24 24" aria-hidden="true"><g fill="none" stroke="#f5ad1b" stroke-width="2"><circle cx="12" cy="12" r="9"/><ellipse cx="12" cy="12" rx="4" ry="9"/><path d="M3 12h18M5 7h14M5 17h14"/></g></svg>
          <span>www.<span class="contact__accent">vitalane</span>.com</span>
        </li>
      </ul>
    </div>
  </section>

</body>
</html>
```